Product label design needed for an odor removal line of products.

I need a label designed for an odor removal product line. There are eight additional odor removal products that I will need labels designed for so the winner will have additional work from me. I would like each of those products to have a similar look and feel in each one. This contest is for one of the products. The Brightwell 417 (would love a better name if you are so inclined -many people know what it is by the 417). The no smell formula does not mask odors, it eliminates odors at their source . Also Reduces Allergens! Simply open silver packet and place in dispenser. Great for use in cars, near pet beds or litter boxes, near diaper pails -anywhere odors are a problem. Lasts 60-90 days. Safe to use. Other uses: Nursing homes, hotel rooms, locker rooms, teenage boy rooms, basements... Eco Friendly! No VOC's or phthalates! Do not consume. Keep out of reach of children and pets. Replace every 60-90 days. I put the picture of my logo , the product as it is packaged and a picture of the actual product and the dispenser it will go in. the package is 4x5 in silver packet with .25 seam on the side and .5 seam on the top and bottom. (Dispenser will have a label with reorder information on it. to be designed later) You do not have to put all information provided on the label. It is to be used as you see fit. I tend to like clean, bold designs but am open to all options. Prefer not to use word air freshener.

Target Market(s)

Men and women between 30-65

Industry/Entity Type

Cleaning Product

Font styles to use
Sans Serif

Colors
acd136
9bcb3c
ffffff

Requirements
Must have
• ability for concept/look to be used for a laundry product, smaller odor elimination pouch, odor removing canister and spray as well
Nice to have
• I like greens but am open to designers to decide
Should not have
• word air freshener

```html
<!DOCTYPE html>
<html lang="en">
<head>
<meta charset="utf-8">
<title>The Brightwell 417 – Packet Label</title>
<link href="https://fonts.googleapis.com/css2?family=Oswald:wght@400;600;700&display=swap" rel="stylesheet">
<style>
  :root {
    --backdrop: #353535;
    --green-deep: #00924a;
    --green-mid: #3fae3b;
    --green-lime: #9bcb3c;
    --green-bright: #acd136;
    --silver-light: #ffffff;
    --silver-shade: #d9dbdd;
    --seal-fill: #5e6166;
    --seal-ring: #eef0f1;
    --white: #ffffff;
    --text-shadow-green: #0b5e2a;
  }
  * { margin: 0; padding: 0; box-sizing: border-box; }
  html, body {
    width: 1200px; height: 565px; overflow: hidden;
    background: var(--backdrop);
  }
  .canvas {
    position: relative; width: 1200px; height: 565px;
    display: flex; align-items: center; justify-content: center;
  }
  .packet-label {
    position: relative; width: 300px; height: 375px;
    box-shadow: 0 2px 6px rgba(0,0,0,.35);
  }
  .packet-label svg.label-art { position: absolute; inset: 0; }
  .product-title {
    position: absolute; top: 74px; left: 0; width: 100%;
    text-align: center; color: var(--white);
    font-family: "Oswald", sans-serif; font-weight: 700;
    font-size: 31px; line-height: 36px; letter-spacing: .2px;
    text-shadow: 2px 2px 0 var(--text-shadow-green);
  }
  .brand-seal {
    position: absolute; left: 71px; top: 114px;
    width: 152px; height: 152px; border-radius: 50%;
    background: var(--seal-fill);
    border: 7px solid var(--seal-ring);
    box-shadow: 0 1px 3px rgba(0,0,0,.25);
    display: flex; align-items: center; justify-content: center;
  }
  .brand-name {
    font-family: "Oswald", sans-serif; font-weight: 400;
    font-size: 23px; line-height: 28px; color: var(--white);
    letter-spacing: 2px; text-transform: uppercase; text-align: center;
  }
  .claims {
    position: absolute; top: 271px; left: 0; width: 100%;
    text-align: center; color: var(--white);
    font-family: "Oswald", sans-serif; font-weight: 400;
    font-size: 21px; line-height: 25px; letter-spacing: -.2px;
    text-shadow: 1px 1px 0 var(--text-shadow-green);
  }
</style>
</head>
<body>
<main class="canvas">
  <section class="packet-label">
    <svg class="label-art" viewBox="0 0 300 375" width="300" height="375" aria-hidden="true">
      <defs>
        <linearGradient id="silver" x1="0" y1="0" x2="0" y2="1">
          <stop offset="0" stop-color="var(--silver-shade)"/>
          <stop offset=".25" stop-color="var(--silver-light)"/>
          <stop offset=".75" stop-color="var(--silver-light)"/>
          <stop offset="1" stop-color="var(--silver-shade)"/>
        </linearGradient>
        <linearGradient id="field" x1="0" y1="0" x2="0" y2="1">
          <stop offset="0" stop-color="var(--green-mid)"/>
          <stop offset=".45" stop-color="var(--green-lime)"/>
          <stop offset="1" stop-color="var(--green-deep)"/>
        </linearGradient>
        <radialGradient id="mist" cx=".5" cy=".5" r=".5">
          <stop offset="0" stop-color="#fff" stop-opacity=".55"/>
          <stop offset="1" stop-color="#fff" stop-opacity="0"/>
        </radialGradient>
      </defs>
      <rect class="silver-stock" width="300" height="375" fill="url(#silver)"/>
      <path class="accent-top" d="M0,70 C25,44 70,40 130,41 C200,42 265,44 300,2 L300,0 L300,10 C265,50 200,50 130,48 C70,47 25,50 0,78 Z" fill="var(--green-bright)"/>
      <path class="green-field" d="M0,74 C25,48 70,44 130,44 C200,45 268,46 300,4 L300,312 C270,334 200,330 120,333 C60,336 20,348 0,375 Z" fill="url(#field)"/>
      <path class="accent-bottom" d="M0,375 C20,348 60,336 120,333 C200,330 270,334 300,312 L300,322 C270,340 200,336 120,339 C60,342 25,354 8,375 Z" fill="var(--green-bright)"/>
      <ellipse class="mist-left" cx="50" cy="150" rx="42" ry="48" fill="url(#mist)"/>
      <ellipse class="mist-right" cx="250" cy="150" rx="42" ry="48" fill="url(#mist)"/>
    </svg>
    <h1 class="product-title">The Brightwell 417</h1>
    <div class="brand-seal">
      <span class="brand-name">Clearleaf<br>Home</span>
    </div>
    <p class="claims">Eco Friendly!<br>No VOC's or phthalates!</p>
  </section>
</main>
</body>
</html>
```